依頼詳細
法人化にともない名刺を作成したいと思っております。シンプル・清潔感・安心感がイメージです。また、企業理念をイメージに取り入れていただけると幸いです。
表面に【リスクマネジメントのプロがサポートする】を入れていただきたいです。
記載項目
表面:会社名/役職/氏名/住所/電話/FAX/携帯/mail 裏面:取扱保険会社/取扱種目 任意労災保険・賠償責任保険・自動車保険・火災保険・生産物品質保険・工事賠償保険・医療保険・地震保険・生命保険・経営者保険 ●その他、多数取り扱っております。お気軽にご相談ください。/取扱保険会社のロゴスペースあれば追加
希望イメージ
シンプル 複雑
単色 カラフル
暗い 明るい
日常 高級
遊び心 厳粛
未来的 伝統的
女性的 男性的
希望する色
青系、水色系、紫系
納品ファイル
補足説明
取扱保険会社(KTR損害保険株式会社・光栄生命保険株式会社)のロゴも添付したします。【裏面スペースあれば】
■ 選んだ理由

最初に希望のイメージをご提案いただきました。また全体のバランスやワンポイントのゴールドがとても気に入りました。

■ 提案者全員のお礼・コメント

ご提案いただきました皆様大変ありがとうございました。とてもすべて素晴らしいデザインばかりで最後まで悩みました。今後も会社として依頼をする事がありますので、その節は宜しくお願い致します。

```html
<!DOCTYPE html>
<html lang="ja">
<head>
<meta charset="utf-8">
<title>Clearbay 名刺 表・裏</title>
<link href="https://fonts.googleapis.com/css2?family=Noto+Sans+JP:wght@400;500;700&family=Roboto:ital,wght@0,400;0,700;1,400;1,700&display=swap" rel="stylesheet">
<style>
:root{
  --paper:#ffffff;
  --ink:#222222;
  --label:#6b6b6b;
  --brand:#3f5fae;
  --brand-soft:#7d8cc6;
  --line:#4a6ab8;
}
*{margin:0;padding:0;box-sizing:border-box}
html,body{width:1200px;height:3888px;overflow:hidden;background:var(--paper)}
body{position:relative;font-family:"Noto Sans JP",sans-serif;color:var(--ink)}
.crop-marks{position:absolute;left:0;top:0}
.side-label{position:absolute;width:352px;height:96px;background:var(--label);color:#fff;font-family:"Roboto",sans-serif;font-size:56px;line-height:96px;text-align:center}
.card{position:absolute;left:192px;width:820px;overflow:hidden}
.card--front{top:340px;height:1388px;background:var(--paper);border:3px solid #333}
.card--back{top:2352px;height:1448px;background:var(--brand-soft);border:3px solid #333}
.abs{position:absolute}

/* front */
.brand-block{left:276px;top:110px;display:flex;align-items:center;gap:24px}
.brand-square{width:72px;height:72px;background:var(--brand)}
.brand-text .tag{font-family:"Roboto",sans-serif;font-size:26px;color:var(--brand)}
.brand-text .name{font-family:"Roboto",sans-serif;font-weight:700;font-size:64px;color:var(--brand);line-height:1}
.motto{right:34px;top:320px;writing-mode:vertical-rl;font-size:38px;line-height:52px;color:var(--brand);letter-spacing:4px}
.motto span{display:block}
.motto span+span{padding-top:96px}
.title{left:36px;top:548px;font-size:34px}
.person-name{left:36px;top:584px;font-size:64px;font-weight:500;letter-spacing:6px}
.name-rule{left:36px;top:662px;width:420px;height:10px;background:linear-gradient(90deg,var(--line),#9db2e6)}
.romaji{left:36px;top:688px;font-size:28px;font-family:"Roboto",sans-serif}
.contact{left:36px;font-size:30px;font-family:"Roboto",sans-serif;display:flex;align-items:center;gap:10px}
.contact svg{width:36px;height:36px}
.company{left:36px;top:1000px;font-size:38px;font-weight:500}
.address{left:36px;top:1058px;font-size:30px;line-height:42px}
.tel-fax{left:36px;top:1200px;font-size:30px;font-family:"Roboto",sans-serif;display:flex;align-items:center;gap:8px;white-space:nowrap}
.tel-fax svg{width:44px;height:44px}

/* back */
.back-oval{left:-20px;top:40px;width:860px;height:1370px;border-radius:50%;background:var(--paper)}
.section-label{left:50%;transform:translateX(-50%);background:var(--brand-soft);color:#fff;font-size:36px;text-align:center;line-height:56px;padding:0 28px;letter-spacing:4px;white-space:nowrap}
.insurers{left:46px;top:296px;width:728px;height:100px;border:3px solid var(--brand-soft);display:flex;align-items:center;justify-content:space-around;font-size:44px;font-weight:700;color:var(--brand);background:var(--paper)}
.insurers .box{border:3px solid var(--brand);padding:0 22px;font-family:"Roboto",sans-serif}
.lines{left:54px;top:512px;width:720px;height:340px;border:3px solid var(--brand-soft);padding:24px 0 0 64px;font-size:34px;line-height:58px;letter-spacing:3px;white-space:nowrap;background:var(--paper)}
.note{left:36px;top:920px;font-size:26px;color:var(--brand);white-space:nowrap}
</style>
</head>
<body>

<svg class="crop-marks" width="1200" height="3888" viewBox="0 0 1200 3888" fill="none" stroke="#333" stroke-width="3" aria-hidden="true">
  <path d="M144 140V292 M192 140V292 M1012 140V292 M1060 140V292 M0 292H144 M0 340H144 M1060 292H1200 M1060 340H1200"/>
  <path d="M144 1776V1930 M192 1776V1930 M1012 1776V1930 M1060 1776V1930 M0 1728H144 M0 1776H144 M1060 1728H1200 M1060 1776H1200"/>
  <path d="M602 200V292 M480 240H724 M602 1776V1880 M480 1836H724 M40 1034H144 M92 900V1170 M1060 1034H1164 M1112 900V1170"/>
  <path d="M144 2160V2304 M192 2160V2304 M1012 2160V2304 M1060 2160V2304 M0 2304H144 M0 2352H144 M1060 2304H1200 M1060 2352H1200"/>
  <path d="M144 3848V3888 M192 3848V3888 M1012 3848V3888 M1060 3848V3888 M0 3800H144 M0 3848H144 M1060 3800H1200 M1060 3848H1200"/>
  <path d="M602 2200V2304 M480 2250H724 M40 3076H144 M92 2940V3210 M1060 3076H1164 M1112 2940V3210"/>
</svg>

<div class="side-label" style="left:200px;top:32px">Front</div>
<div class="side-label" style="left:228px;top:2072px">Back</div>

<section class="card card--front">
  <div class="abs brand-block">
    <div class="brand-text">
      <div class="tag">Insurance Agency</div>
      <div class="name">Clearbay</div>
    </div>
    <div class="brand-square"></div>
  </div>

  <p class="abs motto"><span>リスクマネジメントの</span><span>プロがサポートする</span></p>

  <p class="abs title">代表取締役</p>
  <p class="abs person-name">名刺　太郎</p>
  <div class="abs name-rule"></div>
  <p class="abs romaji">Meishi Taro</p>

  <p class="abs contact" style="top:752px">
    <svg viewBox="0 0 24 24"><rect x="6" y="2" width="12" height="20" rx="2" fill="none" stroke="#222" stroke-width="2"/><rect x="10" y="18" width="4" height="1.5" fill="#222"/></svg>
    : 090-1234-5678
  </p>
  <p class="abs contact" style="top:812px">
    <svg viewBox="0 0 24 24"><rect x="2" y="5" width="20" height="14" fill="#222"/><path d="M2 5l10 8 10-8" stroke="#fff" stroke-width="1.5" fill="none"/></svg>
    : taro@example.co.jp
  </p>

  <p class="abs company">株式会社クリアベイ</p>
  <p class="abs address">〒000-0000<br>東京都□□□□□□□□□□□□□<br>□□□□□□□□□□□□</p>
  <p class="abs tel-fax">
    <svg viewBox="0 0 24 24"><path d="M6 3l3 0 1.5 4.5-2 1.5a12 12 0 0 0 6.5 6.5l1.5-2 4.5 1.5 0 3a2 2 0 0 1-2 2A17 17 0 0 1 4 5a2 2 0 0 1 2-2z" fill="#222"/></svg>
    : 03-0000-0000
    <svg viewBox="0 0 24 24"><rect x="3" y="9" width="18" height="12" fill="#222"/><rect x="7" y="3" width="10" height="7" fill="none" stroke="#222" stroke-width="2"/><rect x="12" y="12" width="6" height="2" fill="#fff"/><rect x="12" y="16" width="6" height="2" fill="#fff"/></svg>
    : 03-0000-0000
  </p>
</section>

<section class="card card--back">
  <div class="abs back-oval"></div>
  <p class="abs section-label" style="top:224px">取扱保険会社</p>
  <div class="abs insurers">
    <span class="box">KTR</span>
    <span>KTR損保</span>
    <span>光栄生命</span>
  </div>
  <p class="abs section-label" style="top:432px;padding:0 64px;letter-spacing:22px">取扱種目</p>
  <div class="abs lines">
    <p>・任意労災保険・賠償責任保険</p>
    <p>・自動車保険・火災保険</p>
    <p>・生産物品質保険・工事賠償保険</p>
    <p>・医療保険・地震保険</p>
    <p>・生命保険・経営者保険</p>
  </div>
  <p class="abs note">●その他、多数取り扱っております。お気軽にご相談ください。</p>
</section>

</body>
</html>
```